Unique Flyer Project - www.plumvaleforms.com.au

The purpose of this flyer is trying to get recipients to visit the website www.plumvaleforms.com.au and sign up to the offer. I need it to be simple/to the point, eye catching and professional. I will post up a basic idea I have but feel free to put your own spin on it if you think you have great ideas to get people to visit the site, if not then just improve upon the quality of mine and make it look like a respected company.

I also think a red band or something that REALLY catches the eye highlighting one of the important aspects of the flyer (the domain?) could be great so even if someone is about to put it in the bin, the popping red-on-white-background catches their eye so they end up looking at and reading the flyer.

I would also love a VERY SIMPLE design for the backside of the flyer, just a red box/band (whatever you think is good) with the domain 'www.plumvaleforms.com.au' in it. NOTHING ELSE! Just so if it's floating around the table and it's upside down, there's something eye catching that might entice the householder to look at it.

DESIGN IS FOR DL FLYER: 99mm X 210mm

Target Market(s)

Australian Residents interested in earning money from home.

Industry/Entity Type

It Company

Requirements
Must have
• Eye catching (mainly red band/box/bar on front & back page), SIMPLE, elegant/professional.
Should not have
• ANYTHING unnecessary to the reader that will distract them from the ultimate point - GET PAID TO DO SURVEYS FROM YOUR OWN HOME ON THE COMPUTER!

```html
<!DOCTYPE html>
<html lang="en">
<head>
<meta charset="utf-8">
<title>Plumvale Forms – DL Flyer, Front and Back</title>
<link rel="stylesheet" href="https://fonts.googleapis.com/css2?family=Oswald:wght@500;700&display=swap">
<style>
  :root {
    --flyer-red: #e0332a;
    --paper-white: #ffffff;
    --ink-black: #111111;
    --stage-grey: #e6e6e6;
    --silhouette-tone: #1a1a1a;
  }
  * { box-sizing: border-box; margin: 0; padding: 0; }
  html, body {
    width: 1200px;
    height: 750px;
    overflow: hidden;
    background: var(--stage-grey);
    font-family: "Oswald", "Arial Narrow", sans-serif;
  }
  .stage {
    width: 1200px;
    height: 750px;
    display: flex;
    justify-content: center;
    align-items: center;
    gap: 70px;
  }
  .flyer {
    width: 302px;
    height: 640px;
    background: var(--paper-white);
    padding: 14px;
    box-shadow: 0 2px 6px rgba(0,0,0,0.12);
  }
  .flyer-band {
    width: 100%;
    height: 100%;
    background: var(--flyer-red);
    position: relative;
    overflow: hidden;
  }

  /* Front */
  .headline {
    position: absolute;
    top: 14px;
    left: 14px;
    right: 10px;
    text-transform: uppercase;
    font-weight: 700;
    line-height: 0.88;
    letter-spacing: 0.3px;
    white-space: nowrap;
  }
  .headline-line { display: block; }
  .headline-get { color: var(--paper-white); font-size: 46px; }
  .headline-paid { color: var(--ink-black); font-size: 64px; }
  .headline-todo { color: var(--paper-white); font-size: 46px; }
  .headline-surveys { color: var(--paper-white); font-size: 64px; }
  .home-worker-illustration {
    position: absolute;
    top: 10px;
    left: 152px;
    width: 112px;
    height: 96px;
    background: linear-gradient(160deg, #2a2a2a, var(--silhouette-tone));
    border-radius: 4px;
  }
  .subline {
    position: absolute;
    top: 216px;
    left: 14px;
    color: var(--ink-black);
    font-weight: 700;
    font-size: 21px;
    line-height: 1.1;
    text-transform: uppercase;
    white-space: nowrap;
  }
  .front-domain {
    position: absolute;
    left: 14px;
    bottom: 16px;
    color: var(--paper-white);
    font-weight: 500;
    font-size: 22px;
    letter-spacing: 0.2px;
    white-space: nowrap;
  }

  /* Back */
  .back-domain {
    position: absolute;
    left: 14px;
    top: 50%;
    transform: translateY(-50%) rotate(180deg);
    writing-mode: vertical-rl;
    color: var(--paper-white);
    font-weight: 700;
    font-size: 50px;
    letter-spacing: 0.5px;
    white-space: nowrap;
  }
</style>
</head>
<body>
  <main class="stage">
    <section class="flyer flyer-front" aria-label="Flyer front">
      <div class="flyer-band">
        <div class="home-worker-illustration" role="img" aria-label="Silhouette of a person working at a computer desk"></div>
        <h1 class="headline">
          <span class="headline-line headline-get">Get</span>
          <span class="headline-line headline-paid">Paid</span>
          <span class="headline-line headline-todo">To Do</span>
          <span class="headline-line headline-surveys">Surveys</span>
        </h1>
        <p class="subline">From your own home<br>on the computer!</p>
        <p class="front-domain">www.plumvaleforms.com.au</p>
      </div>
    </section>

    <section class="flyer flyer-back" aria-label="Flyer back">
      <div class="flyer-band">
        <p class="back-domain">www.plumvaleforms.com.au</p>
      </div>
    </section>
  </main>
</body>
</html>
```